Flyer Design Project

I need a flyer design to pass out to promote my business and to bring in more business. My business is a auto body shop and we do auto body repair on all makes and models. We take all types of insurance work and cash deals are welcome. We type of paint we use is KVX so i would like the KVX logo somewhere on the flyer.I would also like to include that we offer free estimates.
Updates

I forgot to include the following information to my shop

Address : 3846 N. Willowmere Ave
                 San Mateo, Ca 94402

Tel : 650-817-3926

Website : www.KelvoCollision.com

please include that cash deals are welcome, we offer 24 hours drop off service, and we offer mobile estimate service

Industry/Entity Type

Insurance

Requirements
Must have
• Must have my company logo in it. Must be eye catching.

```html
<!DOCTYPE html>
<html lang="en">
<head>
<meta charset="utf-8">
<title>Kelvo Auto Body Shop Flyer</title>
<link rel="stylesheet" href="https://fonts.googleapis.com/css2?family=Montserrat:wght@300;400;600;700&family=Raleway:wght@300;400&display=swap">
<style>
  :root {
    --frame-dark: #1c1c1e;
    --red-core: #e0261f;
    --red-deep: #8e0d0b;
    --silver-light: #f2f2f2;
    --silver-mid: #b9b9bb;
    --silver-dark: #6e6e70;
    --band-black: #151516;
    --text-white: #ffffff;
    --text-soft: #e9e9e9;
    --web-red: #b9201a;
  }
  * { margin: 0; padding: 0; box-sizing: border-box; }
  html, body { width: 857px; height: 1200px; overflow: hidden; background: #ffffff; }
  .flyer {
    position: relative; width: 857px; height: 1200px; overflow: hidden;
    background: var(--frame-dark);
    font-family: "Montserrat", sans-serif;
  }
  .red-panel {
    position: absolute; left: 38px; top: 38px; right: 38px; bottom: 30px;
    background: radial-gradient(ellipse at 45% 45%, var(--red-core) 0%, #c11a15 45%, var(--red-deep) 100%);
  }
  .screw {
    position: absolute; width: 34px; height: 34px; border-radius: 50%;
    background: radial-gradient(circle at 40% 35%, var(--silver-light), var(--silver-dark));
    box-shadow: 0 1px 3px rgba(0,0,0,.6);
  }
  .screw.tl { left: 50px; top: 72px; }
  .screw.tr { right: 50px; top: 72px; }
  .screw.bl { left: 50px; top: 1102px; }
  .screw.br { right: 50px; top: 1102px; }
  .headline {
    position: absolute; top: 56px; left: 0; width: 100%; text-align: center;
    font-weight: 600; font-size: 56px; letter-spacing: 2px; color: var(--silver-light);
    text-shadow: 0 2px 3px rgba(0,0,0,.5);
  }
  .brand {
    position: absolute; left: 70px; top: 200px; width: 380px; text-align: center;
    color: var(--silver-light); font-weight: 700;
  }
  .brand-name { font-size: 96px; line-height: 1; letter-spacing: 2px; }
  .brand-sub { font-size: 40px; line-height: 1.2; }
  .photo-frame {
    position: absolute; left: 370px; top: 258px; width: 487px; height: 541px;
    background: linear-gradient(135deg, var(--silver-light), var(--silver-dark));
    clip-path: polygon(84px 0, 100% 0, 100% 100%, 84px 100%, 0 50%);
  }
  .photo {
    position: absolute; left: 376px; top: 264px; width: 481px; height: 529px;
    background: linear-gradient(120deg, #a89a86 0%, #6e5a4c 40%, #c42a22 75%, #7a1310 100%);
    clip-path: polygon(82px 0, 100% 0, 100% 100%, 82px 100%, 0 50%);
  }
  .badge {
    position: absolute; left: 641px; top: 176px; width: 144px; height: 144px; border-radius: 50%;
    background: radial-gradient(circle at 40% 35%, #ffffff, #a9a9ab);
    border: 4px solid #5b5b5d;
    display: flex; flex-direction: column; align-items: center; justify-content: center;
    transform: rotate(-12deg); color: #222; font-weight: 700; line-height: 1;
  }
  .badge-top { font-size: 30px; }
  .badge-bottom { font-size: 18px; letter-spacing: 1px; }
  .services {
    position: absolute; left: 62px; top: 444px; list-style: none;
    font-family: "Raleway", sans-serif; font-weight: 400; font-size: 18px; line-height: 23.4px;
    color: var(--text-soft);
  }
  .services li { padding-left: 17px; text-indent: -17px; width: 310px; }
  .services li::before { content: "•"; display: inline-block; width: 17px; text-indent: 0; }
  .services li.plain { padding-left: 0; text-indent: 0; }
  .services li.plain::before { content: none; }
  .paint-brand {
    position: absolute; left: 422px; top: 766px; display: flex; align-items: center; gap: 8px;
    font-weight: 700; font-size: 32px; color: var(--text-white);
  }
  .paint-brand .mark { width: 14px; height: 14px; background: var(--text-white); }
  .contact-band {
    position: absolute; left: 0; top: 884px; width: 100%; height: 172px;
    background: linear-gradient(180deg, #2a2a2c, var(--band-black));
  }
  .band-line {
    position: absolute; left: 0; width: 100%; height: 8px;
    background: linear-gradient(180deg, var(--silver-light), var(--silver-dark));
  }
  .band-line.top { top: 880px; }
  .band-line.bottom { top: 1052px; }
  .address {
    position: absolute; top: 916px; width: 100%; text-align: center;
    font-weight: 400; font-size: 25px; color: var(--text-soft);
  }
  .phone {
    position: absolute; top: 966px; width: 100%; text-align: center;
    font-weight: 700; font-size: 36px; color: var(--text-soft);
  }
  .website {
    position: absolute; left: 252px; top: 1022px; width: 353px; height: 52px;
    background: var(--web-red); color: var(--text-white);
    font-weight: 700; font-size: 19px; display: flex; align-items: center; justify-content: center;
  }
  .footer-note {
    position: absolute; top: 1099px; width: 100%; text-align: center;
    font-size: 16px; line-height: 22px; color: var(--text-soft);
  }
</style>
</head>
<body>
<div class="flyer">
  <div class="red-panel"></div>
  <div class="screw tl"></div>
  <div class="screw tr"></div>

  <h1 class="headline">AUTO BODY SHOP</h1>

  <div class="brand">
    <div class="brand-name">KELVO</div>
    <div class="brand-sub">Auto Body Shop</div>
  </div>

  <div class="photo-frame"></div>
  <div class="photo" role="img" aria-label="Technician in a mask repairing the door panel of a red sports car in the workshop"></div>

  <div class="badge">
    <span class="badge-top">FREE</span>
    <span class="badge-bottom">ESTIMATES</span>
  </div>

  <ul class="services">
    <li>Collision Repairs</li>
    <li>All Insurance Work Accepted</li>
    <li>Major and minor accident damage repair</li>
    <li>All Foreign and Domestic makes and models</li>
    <li>Exact frame straightening on premises</li>
    <li>Expert paint matching and refinishing</li>
    <li>Paintless dent repair</li>
    <li>Free damage repair estimates</li>
    <li>Bumper spot refinishing</li>
    <li>Windshield Replacement</li>
    <li>Expert Unibody Reconstruction</li>
    <li>Dent Removal</li>
    <li class="plain">Car Detailing</li>
  </ul>

  <div class="paint-brand"><span class="mark"></span><span>KVX</span></div>

  <div class="contact-band"></div>
  <div class="band-line top"></div>
  <div class="band-line bottom"></div>
  <p class="address">Address : 3846 N. Willowmere Ave , San Mateo, Ca 94402</p>
  <p class="phone">Tel : 650-817-3926</p>
  <div class="website">www.KelvoCollision.com</div>

  <div class="screw bl"></div>
  <div class="screw br"></div>
  <p class="footer-note">Cash deals are welcome • We offer 24 hours drop off service<br>&amp; we offer mobile estimate service</p>
</div>
</body>
</html>
```